Fact Sheets for Insurance

We need a 4 page booklet brochure designed for our insurance business. Each page is A4. We design insurance plans for our Clients and we wish to use the brochure to market and educate our Client and business partners. The business is Halvorsen Brightwick Financial Services. Colour scheme of our logo and stationary is navy blue and metallic gold. The content has been drafted and each page is attached. Please use your creative freedom to make it look professional and modern. We would like graphics, pictures etc to make it more vibrant as well.

Industry/Entity Type

Insurance

```html
<!DOCTYPE html>
<html lang="en">
<head>
<meta charset="utf-8">
<title>Buying TPD Insurance – Cheat Sheet</title>
<link rel="stylesheet" href="https://fonts.googleapis.com/css2?family=Arimo:wght@400;700&family=Archivo:wght@700&display=swap">
<style>
  :root {
    --navy: #145a7e;
    --navy-deep: #1a4f73;
    --slate: #5f7392;
    --ink: #1c1c1c;
    --grey-head: #4e5258;
    --gold: #9a7b3f;
    --page-top: #dfe3ea;
    --page-bottom: #f4f5f8;
    --panel: #d3d8e3;
    --row-alt: #f3f4f7;
    --canvas: #f6f3ea;
  }
  * { box-sizing: border-box; margin: 0; padding: 0; }
  html, body { width: 1200px; height: 1000px; overflow: hidden; background: var(--canvas); }
  body { font-family: "Arimo", Arial, sans-serif; color: var(--ink); }

  .sheet {
    position: absolute; left: 270px; top: 33px; width: 660px; height: 934px;
    background: linear-gradient(180deg, var(--page-top) 0%, #eceef3 45%, var(--page-bottom) 100%);
  }

  .sidebar-cap { position: absolute; left: 31px; top: 81px; width: 34px; height: 77px; background: var(--navy); }
  .sidebar-cap .mark { position: absolute; left: 9px; top: 28px; width: 16px; height: 16px; border: 1px solid rgba(255,255,255,.45); }
  .sidebar-bar { position: absolute; left: 31px; top: 165px; width: 34px; height: 732px; background: var(--navy); }
  .sidebar-label {
    position: absolute; left: 48px; top: 627px; transform: rotate(-90deg); transform-origin: 0 0;
    color: #fff; font-size: 14px; letter-spacing: 11px; white-space: nowrap;
  }

  .contact { position: absolute; right: 148px; top: 31px; text-align: right; color: var(--navy-deep); font-size: 8.6px; line-height: 12px; }
  .brand { position: absolute; left: 516px; top: 50px; width: 104px; text-align: center; }
  .brand-name { color: var(--navy-deep); font-size: 9.5px; font-weight: 400; line-height: 11px; }

  .title { position: absolute; left: 99px; top: 81px; color: var(--navy); font-family: "Archivo", Arial, sans-serif; font-size: 16.8px; font-weight: 700; }
  .section-head { position: absolute; color: var(--grey-head); font-family: "Archivo", Arial, sans-serif; font-size: 13.4px; font-weight: 700; }

  .needs { position: absolute; left: 105px; top: 154px; width: 261px; border-collapse: collapse; font-size: 12.8px; }
  .needs th { background: var(--slate); color: #fff; font-family: "Archivo", Arial, sans-serif; font-size: 13.4px; text-align: left; height: 30px; padding: 0 8px; }
  .needs th.amount { text-align: right; }
  .needs td { height: 30px; padding: 0 6px; }
  .needs tr:nth-child(odd) td { background: var(--row-alt); }
  .needs tr:nth-child(even) td { background: #fff; }
  .needs td.amount { width: 60px; padding-left: 18px; }
  .needs tr.total td { background: transparent; }

  .providers {
    position: absolute; left: 384px; top: 154px; width: 239px; height: 217px;
    background: linear-gradient(90deg, #e7eaf0 0%, var(--panel) 100%);
    list-style: none; padding: 36px 0 0 16px; font-size: 12.8px;
  }
  .providers li, .help-list li { position: relative; padding-left: 20px; }
  .providers li { height: 32px; }
  .providers li::before, .help-list li::before {
    content: ""; position: absolute; left: 0; top: 5px; width: 5px; height: 5px; border: 1px solid #c6cbd4;
  }

  .tips { position: absolute; left: 105px; top: 400px; width: 518px; height: 262px; border: 1px solid #d3d6dc; background: linear-gradient(180deg,#f7f8fa,#fff); list-style: none; padding: 14px 20px 0 12px; font-size: 12.8px; line-height: 16px; }
  .tips li { position: relative; padding-left: 18px; margin-bottom: 16px; }
  .tips svg { position: absolute; left: 0; top: 3px; }

  .intro { position: absolute; left: 106px; top: 705px; font-size: 12.8px; }
  .help-panel { position: absolute; left: 105px; top: 722px; width: 518px; height: 175px; background: linear-gradient(90deg, #f3f4f7 0%, #eef0f4 45%, #dbe1ec 100%); }
  .help-photo { position: absolute; right: 0; top: 0; width: 230px; height: 100%; background: linear-gradient(135deg, #c9d4e6 0%, #9fb2cf 45%, #e9edf4 70%, #7f93b5 100%); opacity: .85; }
  .help-list { position: absolute; left: 0; top: 16px; list-style: none; font-size: 12.8px; line-height: 21px; }
  .help-list li::before { top: 7px; }
  .help-note { position: absolute; left: 1px; top: 126px; width: 340px; font-size: 12.8px; font-style: italic; line-height: 16px; }
</style>
</head>
<body>
<main class="sheet">
  <div class="sidebar-cap"><span class="mark"></span></div>
  <div class="sidebar-bar"></div>
  <div class="sidebar-label">CHEAT SHEET</div>

  <address class="contact" style="font-style:normal">
    Phone: 02 9555 0143<br>
    admin@halvorsenbrightwick.com.au<br>
    Suite 4, 112-118 Harbour Road Marlow NSW 2199
  </address>
  <div class="brand"><p class="brand-name">Halvorsen Brightwick Financial Services</p></div>

  <h1 class="title">BUYING TOTAL AND PERMANENT DISABILITY (TPD) INSURANCE</h1>

  <h2 class="section-head" style="left:105px;top:128px">HOW MUCH DO I NEED?</h2>
  <table class="needs">
    <thead><tr><th>NEED</th><th class="amount">AMOUNT</th></tr></thead>
    <tbody>
      <tr><td>Repaying Debts</td><td class="amount">$</td></tr>
      <tr><td>Medical Expenses</td><td class="amount">$</td></tr>
      <tr><td>Home Modification Costs</td><td class="amount">$</td></tr>
      <tr><td>Other</td><td class="amount">$</td></tr>
      <tr><td></td><td class="amount"></td></tr>
      <tr class="total"><td>TOTAL</td><td class="amount">$</td></tr>
    </tbody>
  </table>

  <h2 class="section-head" style="left:384px;top:129px">WHO OFFERS IT?</h2>
  <ul class="providers">
    <li>Most Superannuation Funds</li>
    <li>Some Private Health Funds</li>
    <li>Some Employers</li>
    <li>Life Insurance Companies</li>
    <li>General Insurance Companies</li>
  </ul>

  <h2 class="section-head" style="left:105px;top:377px">TIPS &amp; TRAPS</h2>
  <ul class="tips">
    <li><svg width="10" height="12" viewBox="0 0 10 12"><path d="M1 7 L4 11 L9 1" fill="none" stroke="var(--navy)" stroke-width="1.6"/></svg>Purchase an “Own Occuation” definition Policy to ensure that you are not tested against your ability to work in “Any Occupation” at claim time.</li>
    <li><svg width="10" height="12" viewBox="0 0 10 12"><path d="M1 7 L4 11 L9 1" fill="none" stroke="var(--navy)" stroke-width="1.6"/></svg>Review what the policy doesn’t cover “Exclusions”. Standard exclusion for most policies is self-inflicted acts.</li>
    <li><svg width="10" height="12" viewBox="0 0 10 12"><path d="M1 7 L4 11 L9 1" fill="none" stroke="var(--navy)" stroke-width="1.6"/></svg>Look to purchase “Long Term” Life Insurance if you think you will need to hold the policy for a number of years. This may save you tens of thousands of dollars over the life of your policy.</li>
    <li><svg width="10" height="12" viewBox="0 0 10 12"><path d="M1 7 L4 11 L9 1" fill="none" stroke="var(--navy)" stroke-width="1.6"/></svg>Ensure the contract is guaranteed to be renewed if you pay your premiums until expiry age.</li>
    <li><svg width="10" height="12" viewBox="0 0 10 12"><path d="M1 7 L4 11 L9 1" fill="none" stroke="var(--navy)" stroke-width="1.6"/></svg>If purchased through Super, you may be liable for a tax bill in the event of a claim</li>
  </ul>

  <h2 class="section-head" style="left:105px;top:684px">WHEN TO CALL A PROFESSIONAL ADVISER?</h2>
  <p class="intro">If you need help:</p>
  <section class="help-panel">
    <div class="help-photo" role="img" aria-label="Photo of an insurance policy document with a pen and reading glasses"></div>
    <ul class="help-list">
      <li>comparing premiums</li>
      <li>reviewing &amp; comparing policy terms and conditions</li>
      <li>matching a policy to suit your occupation</li>
      <li>purchasing “Long Term” Life Insurance</li>
    </ul>
    <p class="help-note">If you want to ensure that you have someone assisting you if a claim is ever needed to be made.</p>
  </section>
</main>
</body>
</html>
```